The Marlowe Method Diet Business Card

The Marlowe Method is a revolutionary new diet approach. We need a fresh, different business card design for The Marlowe Method. We would like the cards lettering and designed match with the color scheme of the logo(Orange,black,grey) and the website. We would like the front of the business card to be the pic of a scale(that people weigh themselves on).We have attached a pic we would like that kind of old school number scale. With the the words "want to lose weight?Eat what you crave! Change how it's made! Get moving! No gym required. Similar to our shirt design. At the Back of the card we would like our logo. My name Dennis Farrow Jr. My telephone number 504-617-2253 my email dfarrowjr@marlowemethod-example.com

Target Market(s)

Everyone who's looking to get into shape

Industry/Entity Type

Health And Wellness

Contact Information for Business Card

Name , company logo, weight scale. Want to have something people talk about that looks so refreshing

Colors
faa54b
f68d4d
000000
b2b2b2

Requirements
Must have
• Weight scale, logo and futuristic look. Nothing plain get creative baby!
Nice to have
• Something that would stand out in a crowd
Should not have
• Be boring or look like any other card or be anything like Brenner diet cards

```html
<!DOCTYPE html>
<html lang="en">
<head>
<meta charset="utf-8">
<title>The Marlowe Method – Business Card</title>
<link href="https://fonts.googleapis.com/css2?family=Source+Sans+3:wght@400;600;700&display=swap" rel="stylesheet">
<style>
  :root {
    --stage-top: #2b2b2b;
    --stage-bottom: #020202;
    --card-white: #f3f3f3;
    --orange: #f68d4d;
    --orange-light: #faa54b;
    --orange-deep: #f0871a;
    --orange-glow: #fbd3a0;
    --ink: #000000;
    --grey: #b2b2b2;
    --white: #ffffff;
    --scale-dark: #2a2a2a;
    --scale-mid: #5a5a5a;
  }
  * { margin: 0; padding: 0; box-sizing: border-box; }
  html, body { width: 1200px; height: 900px; overflow: hidden; }
  body {
    position: relative;
    background: linear-gradient(180deg, var(--stage-top) 0%, #181818 55%, var(--stage-bottom) 100%);
    font-family: "Source Sans 3", "Myriad Pro", sans-serif;
  }
  .card {
    position: absolute;
    top: 184px;
    height: 490px;
    border-radius: 14px;
    overflow: hidden;
    text-align: center;
  }
  /* back side */
  .card-back {
    left: 299px;
    width: 301px;
    background: var(--card-white);
  }
  .brand {
    position: absolute;
    top: 236px; left: 0; right: 0;
    top: 52px;
    display: flex;
    align-items: center;
    justify-content: center;
    gap: 12px;
  }
  .brand-dot {
    width: 40px; height: 40px;
    border-radius: 50%;
    background: var(--orange-light);
  }
  .brand-name {
    font-size: 25px;
    font-weight: 600;
    line-height: 1.05;
    color: var(--ink);
    text-align: left;
  }
  .holder-name {
    position: absolute;
    top: 377px; left: 0; right: 0;
    font-size: 18px;
    font-weight: 600;
    color: var(--orange-deep);
  }
  .contact {
    position: absolute;
    top: 421px; left: 0; right: 0;
    list-style: none;
    font-size: 14px;
    color: var(--ink);
    line-height: 21px;
  }
  .contact li { display: flex; align-items: center; justify-content: center; gap: 3px; }
  .contact svg { flex: none; }

  /* front side */
  .card-front {
    left: 645px;
    width: 305px;
    background: radial-gradient(ellipse 70% 55% at 50% 45%, var(--orange-glow) 0%, var(--orange-light) 45%, var(--orange-deep) 100%);
    color: var(--white);
  }
  .headline {
    position: absolute;
    top: 45px; left: 0; right: 0;
    font-size: 18px;
    font-weight: 600;
    text-transform: uppercase;
  }
  .front-brand {
    position: absolute;
    top: 100px; left: 0; right: 0;
    display: flex;
    flex-direction: column;
    align-items: center;
    gap: 10px;
  }
  .front-brand .brand-dot {
    width: 70px; height: 70px;
    background: var(--white);
  }
  .front-brand .brand-name {
    color: var(--white);
    font-size: 20px;
    text-align: center;
  }
  .taglines {
    position: absolute;
    top: 252px; left: 0; right: 0;
    list-style: none;
    font-size: 16px;
    font-weight: 600;
    line-height: 27.5px;
  }
  .scale-art {
    position: absolute;
    top: 369px;
    left: 112px;
    width: 81px;
    height: 98px;
    border-radius: 14px 14px 10px 10px;
    background: linear-gradient(180deg, var(--scale-mid) 0%, var(--scale-dark) 100%);
  }
</style>
</head>
<body>
  <section class="card card-back" aria-label="Card back">
    <div class="brand">
      <span class="brand-dot"></span>
      <span class="brand-name">The Marlowe<br>Method</span>
    </div>
    <p class="holder-name">Jr. Dennis Farrow</p>
    <ul class="contact">
      <li>
        <svg width="11" height="11" viewBox="0 0 24 24" aria-hidden="true"><path fill="#f68d4d" d="M6.6 10.8a15.1 15.1 0 0 0 6.6 6.6l2.2-2.2c.3-.3.7-.4 1-.2 1.1.4 2.3.6 3.6.6.6 0 1 .4 1 1V20c0 .6-.4 1-1 1A17 17 0 0 1 3 4c0-.6.4-1 1-1h3.5c.6 0 1 .4 1 1 0 1.3.2 2.5.6 3.6.1.3 0 .7-.2 1z"/></svg>
        504-617-2253
      </li>
      <li>
        <svg width="11" height="9" viewBox="0 0 22 16" aria-hidden="true"><rect width="22" height="16" rx="2" fill="#f68d4d"/><path d="M1 1l10 8 10-8" fill="none" stroke="#fff" stroke-width="1.6"/></svg>
        dfarrowjr@marlowemethod-example.com
      </li>
    </ul>
  </section>

  <section class="card card-front" aria-label="Card front">
    <h1 class="headline">Want to lose weight?</h1>
    <div class="front-brand">
      <span class="brand-dot"></span>
      <span class="brand-name">The Marlowe Method</span>
    </div>
    <ul class="taglines">
      <li>Eat what you crave!</li>
      <li>Change how it's made!</li>
      <li>Get moving!</li>
      <li>No gym required</li>
    </ul>
    <div class="scale-art" role="img" aria-label="Old-school dial bathroom scale in black and silver"></div>
  </section>
</body>
</html>
```